Tovani Nightclub

Nightclub flyer., digital single sided, for FB and IG. I included samples of some previous flyers we've used. Sample Info:
TOVANI
FRIDAYS
FRI MAY 1 2020
DJ BRAVURA (club floor)
DJ ZOLT & DJ RAF (residents on the lounge floor)
4372 Birch Street Sacramento
www.tovanimurcott.com for list/VIP inquiries

Target Market(s)

Upscale top 40 crowd but want some cool and artsy like the examples included.

Font styles to use
Sans Serif

Requirements
Must have
• Tovani Logo
Nice to have
• Would be nice if the flyer can be incorporated later with DJ photos (sometimes we will add dj photos to instagram etc). Would like a big city type of feel.
Should not have
• Nothing too sexual.

```html
<!DOCTYPE html>
<html lang="en">
<head>
<meta charset="utf-8">
<title>Tovani Fridays</title>
<link href="https://fonts.googleapis.com/css2?family=Bodoni+Moda:wght@400;600&family=Oswald:wght@500;600&family=Saira+Condensed:wght@500&family=Montserrat:wght@600&display=swap" rel="stylesheet">
<style>
  :root {
    --page: #e6e6ea;
    --night-deep: #1f1744;
    --night-mid: #342a66;
    --night-glow: #4a3f86;
    --white: #ffffff;
    --headline-yellow: #efe46a;
    --band-yellow: #f3dc12;
    --dj-yellow: #f6e200;
    --star-orange: #f0a232;
    --pill-lilac: #8a80d2;
    --pill-red: #de2f60;
    --photo-shirt: #7fa9c4;
    --photo-denim: #3d4f78;
  }
  html, body {
    margin: 0;
    width: 1200px;
    height: 792px;
    overflow: hidden;
    background: var(--page);
  }
  .canvas {
    position: relative;
    width: 1200px;
    height: 792px;
  }
  .flyer {
    position: absolute;
    left: 338px;
    top: 26px;
    width: 524px;
    height: 740px;
    overflow: hidden;
    box-shadow: 0 8px 24px rgba(0,0,0,0.25);
  }
  .city-backdrop {
    position: absolute;
    inset: 0;
    background:
      radial-gradient(ellipse 60% 30% at 50% 72%, var(--night-glow), transparent 70%),
      radial-gradient(ellipse 70% 40% at 40% 20%, var(--night-mid), transparent 75%),
      linear-gradient(180deg, var(--night-mid) 0%, var(--night-deep) 60%, var(--night-deep) 100%);
  }
  .artwork {
    position: absolute;
    inset: 0;
    width: 524px;
    height: 740px;
  }
  .brand-name { font-family: "Bodoni Moda", serif; font-weight: 400; }
  .headline { font-family: "Bodoni Moda", serif; font-weight: 600; }
  .date-line { font-family: "Saira Condensed", sans-serif; font-weight: 500; }
  .lineup { font-family: "Oswald", sans-serif; font-weight: 600; }
  .address { font-family: "Oswald", sans-serif; font-weight: 500; }
  .pill-label, .website { font-family: "Montserrat", sans-serif; font-weight: 600; }
</style>
</head>
<body>
<div class="canvas">
  <div class="flyer">
    <div class="city-backdrop" role="img" aria-label="Night city skyline and crowd photo in deep purple tones"></div>
    <svg class="artwork" viewBox="0 0 524 740" xmlns="http://www.w3.org/2000/svg">
      <defs>
        <linearGradient id="dj-photo-tone" x1="0" y1="0" x2="0" y2="1">
          <stop offset="0" stop-color="#6f86a8"/>
          <stop offset="0.45" stop-color="var(--photo-shirt)"/>
          <stop offset="1" stop-color="var(--photo-denim)"/>
        </linearGradient>
      </defs>

      <!-- brand mark -->
      <g class="brand">
        <circle cx="63" cy="32" r="20" fill="var(--headline-yellow)"/>
        <text class="brand-name" x="63" y="78" text-anchor="middle" font-size="22" fill="var(--white)">TOVANI</text>
      </g>

      <!-- diagonal accent bands (behind) -->
      <g class="accent-bands" fill="var(--band-yellow)">
        <polygon points="0,149 365,92 365,100 0,166"/>
        <polygon points="0,452 310,392 310,398 0,460"/>
      </g>

      <!-- featured DJ photo area -->
      <rect class="dj-photo" role="img" aria-label="Photo of a featured DJ holding studio speakers" x="330" y="84" width="194" height="340" rx="0" fill="url(#dj-photo-tone)" opacity="0.85"/>

      <!-- front accent band -->
      <polygon class="accent-bands" fill="var(--band-yellow)" points="135,481 524,376 524,395 135,490"/>

      <!-- headline -->
      <text class="headline" x="36" y="242" font-size="205" textLength="309" lengthAdjust="spacingAndGlyphs" fill="var(--white)">TOVANI</text>
      <text class="headline" x="13" y="399" font-size="220" textLength="360" lengthAdjust="spacingAndGlyphs" fill="var(--headline-yellow)">FRIDAYS</text>

      <!-- date -->
      <text class="date-line" x="79" y="502" font-size="50" textLength="365" lengthAdjust="spacingAndGlyphs" fill="var(--night-deep)" stroke="var(--white)" stroke-width="1.3">FRIDAY - MAY 1 2020</text>

      <!-- stars -->
      <g class="stars" fill="var(--star-orange)">
        <polygon transform="translate(238,526)" points="0,-7 2,-2.2 7,-2.2 3,1 4.4,6 0,3.1 -4.4,6 -3,1 -7,-2.2 -2,-2.2"/>
        <polygon transform="translate(262,526)" points="0,-7 2,-2.2 7,-2.2 3,1 4.4,6 0,3.1 -4.4,6 -3,1 -7,-2.2 -2,-2.2"/>
        <polygon transform="translate(287,526)" points="0,-7 2,-2.2 7,-2.2 3,1 4.4,6 0,3.1 -4.4,6 -3,1 -7,-2.2 -2,-2.2"/>
      </g>

      <!-- featuring divider -->
      <g class="featuring">
        <line x1="79" y1="560" x2="444" y2="560" stroke="var(--band-yellow)" stroke-width="1"/>
        <rect x="158" y="554" width="206" height="12" rx="6" fill="var(--pill-lilac)"/>
        <text class="pill-label" x="261" y="563" font-size="7" text-anchor="middle" letter-spacing="1.9" fill="var(--white)">SPECIAL EVENING FEATURING</text>
      </g>

      <!-- lineup -->
      <text class="lineup" x="32" y="614" font-size="44" textLength="451" lengthAdjust="spacingAndGlyphs" fill="var(--dj-yellow)">DJ BRAVURA - <tspan>DJ ZOLT</tspan> <tspan fill="var(--white)">&amp;</tspan> DJ RAF</text>

      <!-- address pill -->
      <g class="address-pill">
        <rect x="79" y="636" width="365" height="27" rx="13.5" fill="var(--pill-red)"/>
        <text class="address" x="261.5" y="656" font-size="17" text-anchor="middle" letter-spacing="1.6" fill="var(--white)">4372 BIRCH STREET SACRAMENTO</text>
      </g>

      <!-- website -->
      <text class="website" x="261.5" y="694" font-size="10" text-anchor="middle" letter-spacing="2.6" fill="var(--white)">WWW.TOVANIMURCOTT.COM</text>
    </svg>
  </div>
</div>
</body>
</html>
```